Harrowgate Estates Business Card for Apartment Buildings

Create business cards for resident managers who run apartment buildings. The audience is the public who are searching for apartment rentals, and current residents who live at the apartment building. Key design element will be incorporating the company logo, however, the logo cannot dominate. The building name and manager name are more important than the logo. Current business card design leaves little room for copy, so we may need to reduce the size on the current card to allow for more space for copy.

Target Market(s)

Adults 18-65 years of age, who are looking for an apartment rental, plus current residents who live at our apartment buildings.

Industry/Entity Type

Property Management

Contact Information for Business Card

A major design element will be use of the company logo. Important property and manager contact information must be part of the design. The size of the logo will need to be reduced to make room for building and manager contact copy.

Font styles to use
Sans Serif

Colors
3176b5
000000
959595
ffffff

Requirements
Must have
• 1) Incorporate the company logo.
• 2) Use the company colors (dark blue, black/grey, over white).
• 3) FEATURE THE BUILDING NAME
• 4) FEATURE THE MANAGER NAME
• 5) The company name is less important than BUILDING and MANAGER
• 6) Manager contact information
• **SEE ATTACHED CREATIVE BRIEF**
Nice to have
• 1) Back of card logo watermark
• 2) Ability to write notes on back of carfd
Should not have
• Avoid letting the company logo dominate the card, the building name and manager are more important than the company logo.

```html
<!DOCTYPE html>
<html lang="en">
<head>
<meta charset="utf-8">
<title>Harrowgate Estates – Resident Manager Business Card</title>
<link rel="stylesheet" href="https://fonts.googleapis.com/css2?family=Source+Sans+3:wght@400;600;700&display=swap">
<style>
  :root {
    --brand-blue: #3176b5;
    --brand-blue-deep: #2a5f86;
    --ink: #000000;
    --grey: #959595;
    --paper: #ffffff;
    --backdrop: #f2f2f2;
  }
  * { margin: 0; padding: 0; box-sizing: border-box; }
  html, body {
    width: 1200px;
    height: 1200px;
    overflow: hidden;
    background: var(--backdrop);
    font-family: "Source Sans 3", "Myriad Pro", Arial, sans-serif;
  }
  .card {
    position: absolute;
    left: 220px;
    width: 761px;
    height: 434px;
    background: var(--paper);
    overflow: hidden;
  }
  .card--front { top: 100px; }
  .card--back { top: 665px; }

  /* Front */
  .brand {
    position: absolute;
    left: 62px;
    top: 58px;
    display: flex;
    align-items: center;
    gap: 18px;
  }
  .brand__square {
    width: 52px;
    height: 52px;
    background: var(--brand-blue);
  }
  .brand__name {
    font-size: 36px;
    font-weight: 700;
    color: var(--brand-blue);
    letter-spacing: 0.5px;
    line-height: 1;
  }
  .manager {
    position: absolute;
    left: 70px;
    top: 152px;
  }
  .manager__name {
    font-size: 27px;
    font-weight: 700;
    color: var(--brand-blue);
    line-height: 1.1;
  }
  .manager__title {
    font-size: 16px;
    font-weight: 400;
    color: var(--grey);
    line-height: 1.1;
  }
  .web-tag {
    position: absolute;
    left: 522px;
    top: 228px;
    width: 239px;
    height: 29px;
    background: var(--ink);
    color: var(--paper);
    font-size: 16px;
    display: flex;
    align-items: center;
    justify-content: center;
  }
  .angles {
    position: absolute;
    left: 0;
    top: 0;
    width: 100%;
    height: 100%;
  }
  .contact {
    position: absolute;
    left: 17px;
    top: 307px;
    list-style: none;
    color: var(--paper);
    font-size: 12px;
    line-height: 15.6px;
    text-transform: uppercase;
  }

  /* Back */
  .back-band {
    height: 132px;
    background: var(--brand-blue);
    color: var(--paper);
    font-size: 20px;
    display: flex;
    align-items: center;
    justify-content: center;
  }
  .note-line {
    position: absolute;
    left: 72px;
    width: 617px;
    height: 3px;
    background: var(--grey);
  }
</style>
</head>
<body>

<section class="card card--front">
  <svg class="angles" viewBox="0 0 634 362" preserveAspectRatio="none" aria-hidden="true">
    <polygon points="0,192 444,362 0,362" fill="var(--ink)"/>
    <polygon points="125,192 570,362 444,362 125,240" fill="var(--brand-blue)"/>
    <polygon points="125,227 444,362 420,362 125,240" fill="var(--brand-blue-deep)"/>
  </svg>

  <div class="brand">
    <span class="brand__square"></span>
    <span class="brand__name">HARROWGATE ESTATES</span>
  </div>

  <div class="manager">
    <h1 class="manager__name">MARISOL DELGADO</h1>
    <p class="manager__title">RESIDENT MANAGER</p>
  </div>

  <div class="web-tag">www.harrowgateestates.us</div>

  <ul class="contact">
    <li>Cedar Court Apartments</li>
    <li>4820 Linden Street</li>
    <li>Riverside, CA 92501</li>
    <li>Office: 555-310-2240</li>
    <li>Fax: 555-310-2241</li>
    <li>Cell: 555-310-2242</li>
    <li>Email: marisol@harrowgateest.com</li>
  </ul>
</section>

<section class="card card--back">
  <div class="back-band">www.harrowgateestates.us</div>
  <span class="note-line" style="top:170px"></span>
  <span class="note-line" style="top:215px"></span>
  <span class="note-line" style="top:260px"></span>
  <span class="note-line" style="top:305px"></span>
  <span class="note-line" style="top:350px"></span>
  <span class="note-line" style="top:395px"></span>
</section>

</body>
</html>
```